Artist needs a business card for her pencil portraits and streetscapes

My mum is an artist and does fabulous portraits and sketches with pencil and needs a business card.
She likes designs that are a bit weird or unusual. The winning design will NOT be a slick modern corporate looking logo. It should be a little bit rustic and different. Interesting patterns and textures would be great, it doesn't even need to look like a business card! Come up with something unique!

Target Market(s)

Older clientele looking for family portraits

Industry/Entity Type

Artists

Contact Information for Business Card

Basically just need the name and contact details

Font styles to use
Decorative
Script

Requirements
Must have
• Lena Brodsworth
• Artist
• 0427913562
• lenabrodsworth@quillpost.example
Nice to have
• Weird artistic backgrounds, interesting textures, unusual designs for an artistic woman.
Should not have
• Nothing ultra modern and nothing corporate looking.

```html
<!DOCTYPE html>
<html lang="en">
<head>
<meta charset="utf-8">
<title>Lena Brodsworth – artist</title>
<link rel="stylesheet" href="https://fonts.googleapis.com/css2?family=Stint+Ultra+Condensed&family=Dancing+Script:wght@400&family=Open+Sans:ital,wght@1,400&display=swap">
<style>
  :root {
    --paper: #eceeed;
    --paper-shade: #e3e7e5;
    --paper-rib: rgba(160, 168, 165, 0.16);
    --paper-fleck: rgba(255, 255, 255, 0.55);
    --ink: #454545;
    --ink-soft: #4d4d4d;
    --sketch-light: #d3dad7;
    --sketch-mid: #b7c2be;
    --sketch-deep: #9aa7a3;
  }
  html, body {
    margin: 0;
    padding: 0;
    overflow: hidden;
    background: var(--paper);
  }
  .card {
    position: relative;
    width: 1200px;
    height: 680px;
    overflow: hidden;
    background-color: var(--paper);
    background-image:
      repeating-linear-gradient(0deg, transparent 0 3px, var(--paper-rib) 3px 4px, transparent 4px 7px),
      repeating-linear-gradient(90deg, transparent 0 9px, var(--paper-fleck) 9px 10px, transparent 10px 23px),
      repeating-linear-gradient(2deg, transparent 0 5px, var(--paper-rib) 5px 6px, transparent 6px 11px),
      radial-gradient(ellipse at 60% 40%, var(--paper) 0%, var(--paper-shade) 100%);
  }
  .still-life {
    position: absolute;
    left: 124px;
    top: 22px;
    width: 470px;
    height: 650px;
  }
  .name {
    position: absolute;
    left: 560px;
    width: 620px;
    top: 196px;
    margin: 0;
    text-align: center;
    white-space: nowrap;
    font-family: "Stint Ultra Condensed", serif;
    font-weight: 400;
    font-size: 132px;
    line-height: 1;
    letter-spacing: 1px;
    color: var(--ink);
    -webkit-text-stroke: 2.5px var(--ink);
  }
  .role {
    position: absolute;
    left: 800px;
    width: 290px;
    top: 368px;
    margin: 0;
    text-align: center;
    font-family: "Dancing Script", cursive;
    font-size: 72px;
    line-height: 1;
    color: var(--ink);
  }
  .contact {
    position: absolute;
    left: 564px;
    width: 600px;
    top: 522px;
    margin: 0;
    text-align: center;
    font-family: "Open Sans", sans-serif;
    font-style: italic;
    font-size: 34px;
    line-height: 56px;
    color: var(--ink-soft);
  }
  .contact span { display: block; white-space: nowrap; }
  .contact .email { font-size: 31px; }
</style>
</head>
<body>
  <main class="card">
    <svg class="still-life" viewBox="0 0 470 650" role="img" aria-label="Pencil drawing of poppies on long stems in a floral-patterned vase">
      <defs>
        <radialGradient id="bloomGlow" cx="50%" cy="30%" r="55%">
          <stop offset="0%" stop-color="var(--sketch-mid)" stop-opacity="0.8"/>
          <stop offset="100%" stop-color="var(--sketch-light)" stop-opacity="0"/>
        </radialGradient>
        <linearGradient id="vaseTone" x1="0" y1="0" x2="0" y2="1">
          <stop offset="0%" stop-color="var(--sketch-mid)" stop-opacity="0.35"/>
          <stop offset="55%" stop-color="var(--sketch-mid)" stop-opacity="0.6"/>
          <stop offset="100%" stop-color="var(--sketch-deep)" stop-opacity="0.7"/>
        </linearGradient>
      </defs>
      <rect x="0" y="0" width="470" height="420" fill="url(#bloomGlow)"/>
      <rect x="156" y="405" width="110" height="240" rx="44" fill="url(#vaseTone)"/>
    </svg>

    <h1 class="name">Lena Brodsworth</h1>
    <p class="role">artist</p>
    <p class="contact">
      <span class="phone">phone:0427913562</span>
      <span class="email">lenabrodsworth@quillpost.example</span>
    </p>
  </main>
</body>
</html>
```